Official personalized stationery with official coat of arms

I am looking for custom stationery design such as US letter size (8.5 X 11 or 21.6cm X 27.9cm), email signature (email) and envelope for US letter size (standard envelope no. 10 or 10.5cm X 24.5cm). Inspired by my personal coat of arms and my postal address:

4186 rue des Saules
Levis, Quebec, G7K 3M2
Canada

Ideally a discreet design based on the coat of arms of Lucien Morvand but inspired by my mother's original coat of arms.

Something golden and translucent, simple but tasteful, without overemphasizing the green color. The coat of arms should have green, but not the entire structure of the stationery.

I am also looking for a small official thank you card in half letter size.

The design must be with the Lucien Morvand coat of arms and not the full coat of arms

Target Market(s)

For official communication

Industry/Entity Type

Communication officiel et parlementaire

Font styles to use
Other font styles liked:
• J’aime bien l’écriture comme le logo de la maison Velloze la police pour écrire le nom Velloze

Requirements
Must have
• Simplicity and use the Lucien Morvand coat of arms and not the full coat of arms
Nice to have
• Official and royal appearance as it is an official heraldic title of the British crown
Should not have
• Email and website

```html
<!DOCTYPE html>
<html lang="en">
<head>
<meta charset="utf-8">
<title>Lucien Morvand — Official Stationery</title>
<link href="https://fonts.googleapis.com/css2?family=Playfair+Display:wght@400&display=swap" rel="stylesheet">
<style>
  :root {
    --canvas: #ffffff;
    --paper: #ececee;
    --gold: #a8872e;
    --gold-soft: #c7ab5e;
    --green: #2f5a2c;
    --ink: #555558;
  }
  * { margin: 0; padding: 0; box-sizing: border-box; }
  html, body { width: 1200px; height: 1200px; overflow: hidden; background: var(--canvas); }
  body { position: relative; font-family: "Playfair Display", Georgia, serif; }

  .letterhead { position: absolute; left: 197px; top: 143px; width: 362px; height: 494px; background: var(--paper); }
  .crest-name {
    position: absolute; left: 0; width: 100%; text-align: center;
    color: var(--gold); font-family: "Playfair Display", Georgia, serif; font-weight: 400;
    white-space: nowrap; line-height: 1;
  }
  .letterhead .crest-name { top: 50px; font-size: 13px; letter-spacing: 0.5px; }
  .office-title { position: absolute; top: 97px; width: 100%; text-align: center; color: var(--gold); font-size: 3.8px; letter-spacing: 0.3px; text-transform: uppercase; }
  .office-holder { position: absolute; top: 104px; width: 100%; text-align: center; color: var(--gold); font-size: 2.6px; letter-spacing: 0.2px; text-transform: uppercase; }
  .office-rule { position: absolute; top: 111px; left: 151px; width: 60px; height: 0.5px; background: var(--gold-soft); }

  .letter-date { position: absolute; top: 154px; right: 52px; font-size: 5.4px; color: var(--ink); }
  .letter-greeting { position: absolute; top: 174px; left: 52px; font-size: 5.4px; color: var(--ink); }
  .letter-body { position: absolute; top: 195px; left: 52px; width: 259px; font-size: 5.3px; line-height: 6.85px; color: var(--ink); text-align: justify; }
  .letter-body p { margin-bottom: 6.8px; }
  .letter-closing { position: absolute; top: 347px; left: 52px; font-size: 5.4px; color: var(--ink); }
  .signature { position: absolute; top: 372px; left: 45px; width: 73px; height: 36px; background: linear-gradient(90deg, rgba(168,135,46,0.35), rgba(168,135,46,0.08)); border-radius: 18px 4px 4px 18px; }
  .signatory { position: absolute; top: 416px; left: 57px; font-size: 5px; color: var(--ink); }

  .envelope { position: absolute; left: 593px; width: 410px; height: 181px; background: var(--paper); overflow: hidden; }
  .envelope-front { top: 147px; }
  .envelope-back { top: 375px; }
  .envelope-front .crest-name { top: 40px; left: 22px; width: auto; text-align: left; font-size: 8px; }
  .return-address { position: absolute; color: var(--gold); font-size: 5.4px; line-height: 7px; }
  .envelope-front .return-address { top: 133px; left: 21px; }
  .envelope-back .return-address { top: 133px; left: 0; width: 100%; text-align: center; }
  .envelope-flap { position: absolute; top: 0; left: 0; }
  .envelope-back .crest-name { top: 94px; font-size: 8px; }
  .crest-dot { display: inline-block; width: 4px; height: 4px; border-radius: 50%; background: var(--gold); vertical-align: middle; margin-right: 3px; }
</style>
</head>
<body>

<section class="letterhead">
  <div class="crest-name">Lucien Morvand</div>
  <div class="office-title">The Office of Lucien Morvand</div>
  <div class="office-holder">Her Excellency the Right Honourable Hélène Varrin</div>
  <div class="office-rule"></div>

  <div class="letter-date">July 03, 2025</div>
  <div class="letter-greeting">Dear Mr/Mrs</div>
  <div class="letter-body">
    <p>Lorem ipsum dolor sit amet, consectetuer adipiscing elit, sed diam nonummy nibh euismod tincidunt ut laoreet dolore magna aliquam erat volutpat. Ut wisi enim ad minim veniam, quis nostrud exerci tation ullamcorper suscipit lobortis nisl ut aliquip ex ea commodo consequat.</p>
    <p>Duis autem vel eum iriure dolor in hendrerit in vulputate velit esse molestie consequat, vel illum dolore eu feugiat nulla facilisis at vero eros et accumsan et iusto odio dignissim qui blandit praesent luptatum zzril delenit augue duis dolore te feugait nulla facilisi. Duis autem vel eum iriure dolor in hendrerit in vulputate velit esse molestie consequat, vel illum dolore eu feugiat nulla facilisis at vero eros et accumsan et iusto odio dignissim qui blandit praesent luptatum zzril delenit augue duis dolore te feugait nulla facilisi.</p>
    <p>Duis autem vel eum iriure dolor in hendrerit in vulputate velit esse molestie consequat, vel illum dolore eu feugiat nulla facilisis at vero eros et accumsan et iusto odio dignissim qui blandit praesent luptatum zzril delenit augue duis dolore te feugait nulla facilisi. Duis autem vel eum iriure dolor in hendrerit in vulputate velit esse molestie consequat.</p>
    <p>Lorem ipsum dolor sit amet, consectetuer adipiscing elit, sed diam nonummy nibh euismod tincidunt ut laoreet dolore magna aliquam erat volutpat. Ut wisi enim ad minim veniam, quis nostrud exerci tation ullamcorper suscipit lobortis nisl ut aliquip ex ea commodo consequat.</p>
  </div>
  <div class="letter-closing">Sincerely,</div>
  <div class="signature" role="img" aria-label="Handwritten gold signature"></div>
  <div class="signatory">Corwin Ashby Lisle</div>
</section>

<section class="envelope envelope-front">
  <div class="crest-name"><span class="crest-dot"></span>Lucien Morvand</div>
  <div class="return-address">
    OFFICIAL &amp; PARLIAMENTARY<br>COMMUNICATION<br>4186 rue des Saules, Lévis,<br>Quebec, G7K 3M2, Canada
  </div>
</section>

<section class="envelope envelope-back">
  <svg class="envelope-flap" width="410" height="181" viewBox="0 0 410 181" aria-hidden="true">
    <polygon points="6,5 404,5 205,85" fill="var(--green)"/>
  </svg>
  <div class="crest-name">Lucien Morvand</div>
  <div class="return-address">
    OFFICIAL &amp; PARLIAMENTARY<br>COMMUNICATION<br>4186 rue des Saules, Lévis,<br>Quebec, G7K 3M2, Canada
  </div>
</section>

</body>
</html>
```